Personal creative Biz Card Design

Need personal yet natural and organic design. The cards I have now are well designed but look too commercial. I want more organic FEELING kind of card. I thought having a headshot would make it more personal... but maybe a sketch effect (or line drawing effect) of face better (?). Maybe in a gray or tungsten color?

Target Market(s)

Well, everyone i give card to will have already seen me face-to-face so that is one thing. Mostly yoga students and people interested in improving their fitness or general health. People looking for wellness, a personal fitness trainer, a yoga teacher

Industry/Entity Type

Health And Wellness

Contact Information for Business Card

I provided examples

Requirements
Must have
• My main logo
• My name

```html
<!DOCTYPE html>
<html lang="en">
<head>
<meta charset="utf-8">
<title>Noel Farrow – Business Card</title>
<link rel="stylesheet" href="https://fonts.googleapis.com/css2?family=Exo+2:wght@400;600;700&display=swap">
<style>
  :root {
    --backdrop: #ecebe8;
    --card-white: #ffffff;
    --card-grey: #dcdcdc;
    --leaf-green: #62a033;
    --leaf-green-dark: #4f8a26;
    --leaf-green-light: #8cc152;
    --ink: #3a3a3a;
    --ink-soft: #8a8a8a;
    --rule-light: rgba(255,255,255,0.55);
  }
  * { box-sizing: border-box; margin: 0; padding: 0; }
  html, body {
    width: 1200px; height: 905px; overflow: hidden;
    background: var(--backdrop);
    font-family: "Exo 2", sans-serif;
  }
  .canvas { position: relative; width: 1200px; height: 905px; }

  .card {
    position: absolute; left: 270px; width: 660px; height: 377px;
    background: linear-gradient(120deg, var(--card-white) 0%, #f3f3f3 55%, var(--card-grey) 100%);
    box-shadow: 0 6px 18px rgba(0,0,0,0.18);
    overflow: hidden;
  }
  .card--front { top: 50px; }
  .card--back { top: 477px; }

  /* front */
  .front__art {
    position: absolute; left: 40px; top: 45px; width: 200px; height: 290px;
    border-radius: 40% 40% 50% 50%;
    background: radial-gradient(ellipse at 50% 85%, rgba(98,160,51,0.35), rgba(98,160,51,0) 60%),
                linear-gradient(180deg, rgba(140,193,82,0.25), rgba(90,90,90,0.12));
  }
  .front__brand { position: absolute; left: 300px; top: 160px; }
  .brand-name {
    display: flex; align-items: center; gap: 12px;
    color: var(--leaf-green); font-weight: 700; letter-spacing: 1px;
  }
  .brand-name__dot { width: 14px; height: 14px; border-radius: 50%; background: var(--leaf-green); }
  .front__brand .brand-name { font-size: 46px; }
  .tagline { color: var(--ink-soft); font-size: 13px; letter-spacing: 0.5px; margin-top: 4px; }
  .front__brand .tagline { margin-left: 26px; }

  /* back */
  .back__identity { position: absolute; left: 38px; top: 110px; width: 270px; }
  .back__identity .brand-name { font-size: 30px; gap: 8px; }
  .back__identity .brand-name__dot { width: 10px; height: 10px; }
  .back__identity .tagline { font-size: 9px; margin-left: 18px; }
  .person { position: absolute; left: 95px; top: 298px; }
  .person__name { color: var(--leaf-green); font-size: 20px; font-weight: 600; letter-spacing: 1px; }
  .person__role { color: var(--ink); font-size: 9px; font-weight: 600; letter-spacing: 1.5px; margin-top: 2px; }

  .contact-panel {
    position: absolute; left: 330px; top: 0; width: 330px; height: 377px;
    background: linear-gradient(160deg, var(--leaf-green-light) 0%, var(--leaf-green) 45%, var(--leaf-green-dark) 100%);
  }
  .contact-panel::before {
    content: ""; position: absolute; left: 62px; top: 0; bottom: 0; width: 1px; background: var(--rule-light);
  }
  .contact-row {
    position: absolute; left: 0; width: 330px; height: 94px;
    display: flex; align-items: center;
    border-bottom: 1px solid var(--rule-light);
  }
  .contact-row:last-child { border-bottom: none; }
  .contact-row__icon { width: 62px; display: flex; justify-content: center; }
  .contact-row__text { padding-left: 18px; color: #fff; font-size: 14px; line-height: 1.35; letter-spacing: 0.5px; }
  .contact-row--phone .contact-row__icon svg { background: #fff; padding: 7px; }
</style>
</head>
<body>
<main class="canvas">

  <section class="card card--front">
    <div class="front__art" role="img" aria-label="Soft green brand illustration area with a sprouting figure motif"></div>
    <div class="front__brand">
      <div class="brand-name"><span class="brand-name__dot"></span>NOEL FARROW</div>
      <p class="tagline">yoga and wellness for body and mind</p>
    </div>
  </section>

  <section class="card card--back">
    <div class="back__identity">
      <div class="brand-name"><span class="brand-name__dot"></span>NOEL FARROW</div>
      <p class="tagline">yoga and wellness for body and mind</p>
    </div>
    <div class="person">
      <p class="person__name">LENA HART</p>
      <p class="person__role">GENERAL MANAGER</p>
    </div>

    <div class="contact-panel">
      <div class="contact-row contact-row--phone" style="top:0">
        <div class="contact-row__icon">
          <svg width="34" height="34" viewBox="0 0 24 24"><path fill="#62a033" d="M6.6 10.8a15.1 15.1 0 0 0 6.6 6.6l2.2-2.2c.3-.3.7-.4 1-.2 1.1.4 2.3.6 3.6.6.6 0 1 .4 1 1V20c0 .6-.4 1-1 1A17 17 0 0 1 3 4c0-.6.4-1 1-1h3.5c.6 0 1 .4 1 1 0 1.3.2 2.5.6 3.6.1.3 0 .7-.2 1z"/></svg>
        </div>
        <div class="contact-row__text">014 552 7310<br>014 552 7311</div>
      </div>
      <div class="contact-row" style="top:94px">
        <div class="contact-row__icon">
          <svg width="24" height="18" viewBox="0 0 24 18"><rect x="1" y="1" width="22" height="16" fill="none" stroke="#fff" stroke-width="2"/><path d="M1 1l11 9 11-9" fill="none" stroke="#fff" stroke-width="2"/></svg>
        </div>
        <div class="contact-row__text">hello@noelfarrow.com</div>
      </div>
      <div class="contact-row" style="top:188px">
        <div class="contact-row__icon">
          <svg width="24" height="24" viewBox="0 0 24 24" fill="none" stroke="#fff" stroke-width="1.8"><circle cx="12" cy="12" r="10"/><ellipse cx="12" cy="12" rx="4.5" ry="10"/><path d="M2 12h20M4 6.5h16M4 17.5h16"/></svg>
        </div>
        <div class="contact-row__text">www.noelfarrowyoga.com</div>
      </div>
      <div class="contact-row" style="top:282px">
        <div class="contact-row__icon">
          <svg width="26" height="24" viewBox="0 0 26 24"><path fill="#fff" d="M13 1 1 12h3.5v11h6.5v-7h4v7h6.5V12H25z"/></svg>
        </div>
        <div class="contact-row__text">27 Willow Lane,<br>Garden Court West</div>
      </div>
    </div>
  </section>

</main>
</body>
</html>
```